Tidewell Pronto Clinic Business card

We want a business card that matches our business theme. Our website is www.prontoclinicbz.example
The company name is Tidewell Pronto Clinic
The persons having the business cards will be doctors
My logo is attached.
We have a drive-thru medical center where our motto is Fast, Reliable, and Convenient. Our goal is to change the medical space while utilizing technologies, keeping a professional and clean look

Medical

Info on the card should be: Name, Position, Cell number, website, email address, possibly the office line as well

• Logo
• Professional medical feel with our logo colors incorporated

```html
<!DOCTYPE html>
<html lang="en">
<head>
<meta charset="utf-8">
<title>Tidewell Pronto Clinic Business Card</title>
<link href="https://fonts.googleapis.com/css2?family=Jost:wght@400;500;600;700&display=swap" rel="stylesheet">
<style>
  :root {
    --backdrop: #cce8f3;
    --card: #ffffff;
    --navy: #1a46a0;
    --sky: #42c8f4;
    --map: #f1f3f6;
  }
  * { box-sizing: border-box; margin: 0; padding: 0; }
  html, body { width: 1200px; height: 1200px; overflow: hidden; }
  body {
    background: var(--backdrop);
    font-family: "Jost", "Futura", sans-serif;
    position: relative;
  }
  .card {
    position: absolute;
    left: 273px;
    width: 654px;
    height: 374px;
    background: var(--card);
    box-shadow: 0 8px 14px rgba(40, 70, 90, 0.28);
    overflow: hidden;
  }
  .card-front { top: 163px; }
  .card-back { top: 633px; }
  .map-texture {
    position: absolute;
    border-radius: 40px;
    background: radial-gradient(ellipse at center, var(--map) 0%, rgba(241,243,246,0) 70%);
  }
  .brand {
    position: absolute;
    display: flex;
    align-items: center;
    gap: 12px;
  }
  .brand-name {
    color: var(--navy);
    font-weight: 700;
    line-height: 1.02;
    white-space: nowrap;
  }
  .brand-mark {
    border-radius: 50%;
    background: var(--navy);
    flex: none;
  }
  /* front */
  .card-front .brand { left: 200px; top: 122px; }
  .card-front .brand-name { font-size: 27px; }
  .card-front .brand-mark { width: 82px; height: 82px; }
  .front-url {
    position: absolute;
    left: 0; right: 0; top: 324px;
    text-align: center;
    color: var(--navy);
    font-weight: 600;
    font-size: 19px;
    letter-spacing: 5px;
    white-space: nowrap;
  }
  /* back */
  .contact-band {
    position: absolute;
    left: 0;
    width: 317px;
    height: 94px;
    display: flex;
    align-items: center;
    padding-left: 33px;
    font-weight: 600;
    font-size: 18px;
    line-height: 1.15;
  }
  .contact-band.dark { background: var(--navy); color: #fff; }
  .contact-band.light { background: var(--sky); color: var(--navy); }
  .band-phone { top: 0; }
  .band-email { top: 94px; }
  .band-web { top: 188px; font-size: 17px; }
  .band-address { top: 282px; height: 92px; text-transform: uppercase; }
  .icon-disc {
    position: absolute;
    left: 280px;
    width: 75px;
    height: 75px;
    border-radius: 50%;
    border: 3px solid #fff;
    display: flex;
    align-items: center;
    justify-content: center;
  }
  .icon-disc.dark { background: var(--navy); }
  .icon-disc.light { background: var(--sky); }
  .icon-disc svg { width: 40px; height: 40px; }
  .holder-name {
    position: absolute;
    left: 396px; top: 46px;
    color: var(--navy);
    font-weight: 700;
    font-size: 27px;
    letter-spacing: 0.5px;
  }
  .holder-role {
    position: absolute;
    left: 396px; top: 90px;
    color: var(--navy);
    font-weight: 500;
    font-size: 21px;
  }
  .card-back .brand { left: 400px; top: 236px; }
  .card-back .brand-name { font-size: 22px; }
  .card-back .brand-mark { width: 72px; height: 72px; }
</style>
</head>
<body>

<section class="card card-front" aria-label="Business card front">
  <div class="map-texture" role="img" aria-label="Faint world map texture" style="left:0;top:0;width:654px;height:300px;"></div>
  <div class="brand">
    <div class="brand-name">Tidewell<br>Pronto Clinic</div>
    <div class="brand-mark"></div>
  </div>
  <p class="front-url">WWW.PRONTOCLINICBZ.EXAMPLE</p>
</section>

<section class="card card-back" aria-label="Business card back">
  <div class="map-texture" role="img" aria-label="Faint world map texture" style="left:340px;top:80px;width:314px;height:294px;"></div>

  <div class="contact-band dark band-phone">501-555-0147</div>
  <div class="contact-band light band-email">tpc@pronto.example</div>
  <div class="contact-band dark band-web">www.prontoclinicbz.example</div>
  <div class="contact-band light band-address">42 Harbour Lane,<br>Belmopan</div>

  <div class="icon-disc dark" style="top:10px;">
    <svg viewBox="0 0 40 40" fill="none" stroke="#fff" stroke-width="1.6">
      <circle cx="20" cy="20" r="17"/>
      <path d="M14 11 l4 0 l1.5 5 l-2.5 2 q2 4.5 6 6.5 l2 -2.5 l5 1.5 l0 4 q-1 2 -4 1.5 q-10 -3 -13.5 -13.5 q-0.5 -3 1.5 -4.5z" stroke-linejoin="round"/>
    </svg>
  </div>
  <div class="icon-disc light" style="top:104px;">
    <svg viewBox="0 0 40 40" fill="none" stroke="#1a46a0" stroke-width="2.4" stroke-linejoin="round">
      <rect x="3" y="9" width="34" height="22" fill="#1a46a0"/>
      <path d="M4 10 L20 23 L36 10" stroke="#42c8f4"/>
      <path d="M4 30 L15 19 M36 30 L25 19" stroke="#42c8f4"/>
    </svg>
  </div>
  <div class="icon-disc dark" style="top:198px;">
    <svg viewBox="0 0 40 40" fill="none" stroke="#fff" stroke-width="2">
      <circle cx="20" cy="20" r="16"/>
      <ellipse cx="20" cy="20" rx="7" ry="16"/>
      <line x1="20" y1="4" x2="20" y2="36"/>
      <line x1="4" y1="20" x2="36" y2="20"/>
      <path d="M7 12 H33 M7 28 H33"/>
    </svg>
  </div>
  <div class="icon-disc light" style="top:292px;">
    <svg viewBox="0 0 40 40">
      <path d="M20 37 C12 26 8 21 8 15 A12 12 0 0 1 32 15 C32 21 28 26 20 37Z" fill="#1a46a0"/>
      <circle cx="20" cy="15" r="4.5" fill="#42c8f4"/>
    </svg>
  </div>

  <h1 class="holder-name">DR. LOREM IPUM</h1>
  <p class="holder-role">DOCTOR</p>

  <div class="brand">
    <div class="brand-name">Tidewell<br>Pronto Clinic</div>
    <div class="brand-mark"></div>
  </div>
</section>

</body>
</html>
```